Lanternway 7.5 - Educational Guide/Course-pack/Worksheet

Our Lanternway 7.5 toolkit is an educational workshop that focuses on inspiring student initiatives in the classroom! We need a new educational course guide or course-pack for students/teachers that clearly outlines or explains the program steps, offers helpful tips and includes empty spaces/lines where their can write down their great ideas or notes. This will include a;

- Teachers Guide (1 Page)
- Student Guide/Worksheet (4 Pages)
- Group Pack Resources (3 Pages)

This will consist of designing/formatting text, stock animation/icons, font, etc. We have included our new logo (color, branding, etc.) and all of the text for each separate course-pack. We have also attached our new website to give you an idea of the program style.

Our workshop can be for any school project like Technology, Community, Environment, Art, Science, etc.

Target Market(s)

High School Students/Teachers

Industry/Entity Type

Education

Font styles to use
Sans Serif

Colors
f68e4e
acd037
34a7d8

Requirements
Must have
• Use our brand colors from logo.
Should not have
• Should not be too childish.

```html
<!DOCTYPE html>
<html lang="en">
<head>
<meta charset="utf-8">
<title>The Money Machines – Financial Needs</title>
<link href="https://fonts.googleapis.com/css2?family=Roboto:wght@400;500;700;900&family=Handlee&display=swap" rel="stylesheet">
<style>
  :root {
    --orange: #f68e4e;
    --orange-deep: #f26f3c;
    --orange-gold: #f8a020;
    --green: #acd037;
    --green-soft: #d8e8a4;
    --green-text: #76a03a;
    --blue: #34a7d8;
    --blue-soft: #a3d0e6;
    --blue-text: #1a86ad;
    --purple: #7b3a8d;
    --purple-soft: #cba8d4;
    --purple-text: #a55bb5;
    --sheet: #e6e7e9;
    --ink: #3a3a3a;
    --muted: #7a7a7a;
    --rule: #c9c9c9;
    --rule-strong: #a9a9a9;
    --pen: #19a4e0;
  }
  * { box-sizing: border-box; margin: 0; padding: 0; }
  html, body { width: 849px; height: 1200px; overflow: hidden; background: #fff; }
  body { position: relative; font-family: "Roboto", Arial, sans-serif; color: var(--ink); }

  .frame {
    position: absolute; left: 32px; top: 30px; width: 772px; height: 1116px;
    background: var(--sheet);
    border-right: 2px solid var(--orange-gold);
    border-bottom: 7px solid var(--orange-gold);
  }
  .banner {
    position: absolute; left: 0; top: 0; width: 770px; height: 69px;
    background: linear-gradient(90deg, var(--orange-deep), var(--orange-gold));
  }
  .inner-outline {
    position: absolute; left: 13px; top: 12px; width: 745px; height: 1080px;
    border: 1.5px solid #fff; border-radius: 12px;
  }
  .title {
    position: absolute; left: 57px; top: 24px;
    font-weight: 900; font-size: 31px; letter-spacing: 1px; color: #fff;
  }
  .section-title {
    position: absolute; left: 57px; top: 101px;
    font-weight: 700; font-size: 18px; color: var(--orange-deep);
  }
  .intro {
    position: absolute; left: 57px; top: 138px; width: 700px;
    font-size: 14.4px; line-height: 18.5px; color: var(--ink);
  }

  .project-bar {
    position: absolute; left: 57px; top: 185px; width: 655px; height: 40px;
    display: flex; border-radius: 9px; overflow: hidden;
    box-shadow: 0 1px 3px rgba(0,0,0,.25);
  }
  .project-bar .label {
    background: #f1f1f1; font-weight: 700; font-size: 13px; letter-spacing: .6px;
    color: var(--green-text); display: flex; align-items: center; padding-left: 12px;
  }
  .project-bar .field { background: #fff; position: relative; }
  .project-bar .field::after {
    content: ""; position: absolute; left: 10px; right: 10px; bottom: 8px;
    border-bottom: 1.5px dotted #999;
  }

  .tab {
    position: absolute; left: 55px; height: 28px; padding: 0 12px;
    border: 4px solid; border-bottom: none; border-radius: 8px 8px 0 0;
    color: #fff; font-weight: 700; font-size: 13.5px; letter-spacing: 1px;
    display: flex; align-items: center;
  }
  .panel {
    position: absolute; left: 55px; width: 658px;
    background: #fff; border: 4px solid; border-radius: 0 8px 8px 8px;
    box-shadow: 1px 2px 4px rgba(0,0,0,.15);
    padding: 0 11px 0 10px;
  }
  .income-tab { top: 240px; background: var(--green); border-color: var(--green-soft); width: 82px; }
  .income { top: 268px; height: 286px; border-color: var(--green-soft); }
  .expenses-tab { top: 572px; background: var(--blue); border-color: var(--blue-soft); width: 96px; }
  .expenses { top: 599px; height: 287px; border-color: var(--blue-soft); }
  .total-tab { top: 907px; background: var(--purple); border-color: var(--purple-soft); width: 73px; }
  .total { top: 934px; height: 127px; border-color: var(--purple-soft); }

  table { width: 629px; border-collapse: collapse; table-layout: fixed; }
  th {
    height: 23px; font-size: 13px; font-weight: 700; letter-spacing: .5px;
    border-bottom: 2px solid var(--rule-strong); vertical-align: middle;
  }
  td {
    height: 23px; text-align: center; vertical-align: middle;
    border-bottom: 1px solid var(--rule);
    font-family: "Handlee", cursive; font-size: 13px; letter-spacing: 1.2px; color: var(--pen);
  }
  th + th, td + td { border-left: 1.5px solid var(--rule); }
  tr.foot td {
    height: 25px; border-bottom: none;
    font-family: "Roboto", Arial, sans-serif; font-weight: 700; font-size: 13px;
    letter-spacing: .6px; color: var(--muted);
  }
  tr.foot td.stars { letter-spacing: 2px; font-weight: 400; padding-top: 2px; }
  .income th { color: var(--green-text); }
  .expenses th { color: var(--blue-text); }
  .total th { color: var(--purple-text); }
</style>
</head>
<body>
  <div class="frame">
    <div class="banner"></div>
    <div class="inner-outline"></div>
    <h1 class="title">The Money Machines</h1>
    <h2 class="section-title">FINANCIAL NEEDS</h2>
    <p class="intro">Make money your friend- not your enemy!&nbsp; You’ve got to know what you need and how much it costs!<br>Ex.&nbsp; Doers realize that they will need 6 soccer-balls, 100 drinks, 2 referee sweaters, etc.</p>

    <div class="project-bar">
      <div class="label" style="width:111px">Project name:</div>
      <div class="field" style="width:317px"></div>
      <div class="label" style="width:56px;padding-left:14px">Date:</div>
      <div class="field" style="width:171px"></div>
    </div>

    <div class="tab income-tab">INCOME</div>
    <section class="panel income">
      <table>
        <colgroup><col style="width:370px"><col style="width:167px"><col style="width:92px"></colgroup>
        <tr><th>Item</th><th>Amount</th><th>Total</th></tr>
        <tr><td>Sponsorships or Donations</td><td></td><td>$ 500</td></tr>
        <tr><td>School Help</td><td></td><td>$ 50</td></tr>
        <tr><td>Sales</td><td></td><td>$ 100</td></tr>
        <tr><td></td><td></td><td></td></tr>
        <tr><td></td><td></td><td></td></tr>
        <tr><td></td><td></td><td></td></tr>
        <tr><td></td><td></td><td></td></tr>
        <tr><td></td><td></td><td></td></tr>
        <tr><td></td><td></td><td></td></tr>
        <tr><td></td><td></td><td></td></tr>
        <tr class="foot"><td class="stars">****************</td><td>Total $ Needed</td><td></td></tr>
      </table>
    </section>

    <div class="tab expenses-tab">EXPENSES</div>
    <section class="panel expenses">
      <table>
        <colgroup><col style="width:267px"><col style="width:103px"><col style="width:167px"><col style="width:92px"></colgroup>
        <tr><th>Item</th><th>Quantity</th><th>Amount</th><th>Total</th></tr>
        <tr><td>Soccer balls</td><td>6</td><td>Free from school</td><td>$&nbsp; 0</td></tr>
        <tr><td>Drinks</td><td>100</td><td>50 cents</td><td>$&nbsp; 50</td></tr>
        <tr><td></td><td></td><td></td><td></td></tr>
        <tr><td></td><td></td><td></td><td></td></tr>
        <tr><td></td><td></td><td></td><td></td></tr>
        <tr><td></td><td></td><td></td><td></td></tr>
        <tr><td></td><td></td><td></td><td></td></tr>
        <tr><td></td><td></td><td></td><td></td></tr>
        <tr><td></td><td></td><td></td><td></td></tr>
        <tr><td></td><td></td><td></td><td></td></tr>
        <tr class="foot"><td class="stars">****************</td><td class="stars">********</td><td>Total $ Needed</td><td></td></tr>
      </table>
    </section>

    <div class="tab total-tab">TOTAL</div>
    <section class="panel total">
      <table>
        <colgroup><col style="width:370px"><col style="width:167px"><col style="width:92px"></colgroup>
        <tr><th>Item</th><th>Amount</th><th>Total</th></tr>
        <tr><td>Income</td><td></td><td></td></tr>
        <tr><td>Expenses</td><td></td><td></td></tr>
        <tr><td></td><td></td><td></td></tr>
        <tr class="foot"><td>(Total 1 – Total 2)</td><td>Total $ Needed</td><td></td></tr>
      </table>
    </section>
  </div>
</body>
</html>
```